Marlowick APP redesign and color change

I am looking for a new design for my app. Please see the attached current design.

Currently, I have a functioning app but the colors and design are awful!
The logo is great but the rest of the app needs a refresh.
(Logo hi res not yet available but will upload soon.)
New colors or anything that is cutting edge.

Basically: It is a secure social media app within a school system where the teachers, students and parents can text, exchange photos, plan curriculum, etc.

I NEED ONLY landing page with a new look!
Looking for one distinct design for the landing page with new look.
The developer will apply this one design towards the rest of the pages/app screens.

Because part of the social media I need the feel and look of what is now the trend. Something that will attract and keep the client(s) interested. I am really leaving all the creative work to the designer and open to any suggestions.
Updates

Target Market(s)

Schools, community, teachers, students, colleges, sport teams

Industry/Entity Type

Non Profit

Font styles to use
Serif
Sans Serif

Colors

Designer to choose colors to be used in the design.

Requirements
Must have
• Sharp, trendy, millennial feel
Nice to have
• Up to designer
Should not have
• Up to designer

```html
<!DOCTYPE html>
<html lang="en">
<head>
<meta charset="utf-8">
<title>Marlowick – App Screens</title>
<link href="https://fonts.googleapis.com/css2?family=Roboto:wght@400;500;700&display=swap" rel="stylesheet">
<style>
:root{
  --stage:#4b4b4b;
  --splash-a:#2a48c9;
  --splash-b:#1e36a6;
  --brand-blue:#0a6fe3;
  --accent:#ff9600;
  --white:#ffffff;
  --ink:#333333;
  --muted:#666666;
  --rule:#e3e3e3;
  --avatar:#8f8f8f;
  --nav-bg:#f4f4f4;
  --nav-icon:#6d6d6d;
  --link:#8fd3ff;
}
*{box-sizing:border-box;margin:0;padding:0}
html,body{width:1200px;height:857px;overflow:hidden}
body{background:var(--stage);font-family:"Roboto",sans-serif;position:relative}
.screen{position:absolute;top:154px;width:298px;height:527px;overflow:hidden;border-radius:2px}
.screen--splash{left:89px;background:radial-gradient(ellipse at 50% 35%,var(--splash-a),var(--splash-b) 75%)}
.screen--login{left:477px;background:var(--brand-blue)}
.screen--chats{left:843px;background:var(--white)}
.status-bar{height:16px;display:flex;align-items:center;justify-content:space-between;padding:0 7px;color:var(--white);font-size:7px;font-weight:500}
.status-bar .signal{letter-spacing:-1px;font-size:6px}
.battery{display:inline-block;width:14px;height:6px;border:1px solid var(--white);border-radius:1px;vertical-align:middle;margin-left:2px;background:linear-gradient(90deg,var(--white) 80%,transparent 80%)}

/* splash */
.splash-brand{position:absolute;top:200px;left:0;right:0;text-align:center;color:var(--white)}
.brand-dot{width:54px;height:54px;border:4px solid var(--white);border-radius:50%;margin:0 auto 26px}
.splash-name{font-size:17px;font-weight:700;letter-spacing:12px;padding-left:12px}
.splash-tagline{margin-top:14px;font-size:10.5px;letter-spacing:.6px}

/* login */
.login-brand{position:absolute;top:88px;left:0;right:0;text-align:center;color:var(--white)}
.login-brand .brand-dot{width:60px;height:60px;margin-bottom:14px}
.login-brand .name{font-size:17px;font-weight:700;letter-spacing:6px;padding-left:6px}
.field{position:absolute;left:54px;width:188px;height:31px;background:var(--white);border-radius:5px;display:flex;align-items:center;padding:0 6px;gap:8px;color:#8a8a8a;font-size:10.5px}
.field--email{top:231px}
.field--pin{top:286px}
.field .trail{margin-left:auto}
.btn-login{position:absolute;left:93px;top:341px;width:111px;height:31px;background:var(--accent);color:var(--white);border:none;font:400 13px "Roboto",sans-serif;display:flex;align-items:center;justify-content:center}
.forgot{position:absolute;top:397px;left:0;right:0;text-align:center;color:var(--white);font-size:10.5px}
.forgot u{text-underline-offset:2px}
.signup{position:absolute;top:480px;left:0;right:0;text-align:center;color:var(--link);font-size:10.5px}
.signup b{font-weight:700;text-decoration:underline;margin:0 2px}

/* chats */
.chat-header{height:52px;background:var(--brand-blue)}
.toolbar{display:flex;align-items:center;justify-content:space-between;padding:6px 8px 0}
.tabs{display:flex;border:1px solid var(--accent);border-radius:2px}
.tab{width:49px;height:16px;font-size:7px;color:var(--accent);display:flex;align-items:center;justify-content:center;border-left:1px solid var(--accent)}
.tab:first-child{border-left:none;background:var(--accent);color:var(--white)}
.chat-list{list-style:none;padding:0 14px 0 14px}
.chat-item{height:51px;display:flex;align-items:center;border-bottom:1px solid var(--rule);padding-left:0}
.avatar{width:46px;height:46px;border-radius:50%;background:var(--avatar);flex:none;margin-right:16px}
.chat-body{flex:1;min-width:0}
.chat-top{display:flex;justify-content:space-between;align-items:baseline;font-size:11px;color:var(--ink)}
.chat-top b{font-weight:500}
.chat-time{font-size:9.5px;color:var(--muted)}
.chat-preview{margin-top:6px;font-size:7px;color:var(--muted)}
.tab-bar{position:absolute;left:0;right:0;bottom:0;height:54px;background:var(--nav-bg);display:flex;justify-content:space-around;align-items:center;padding-top:4px}
.tab-bar__item{display:flex;flex-direction:column;align-items:center;font-size:6px;color:var(--nav-icon);gap:3px}
</style>
</head>
<body>

<section class="screen screen--splash" aria-label="Splash screen">
  <div class="status-bar"><span class="signal">●●●●● ︎</span><span>11:47</span><span>86% <i class="battery"></i></span></div>
  <div class="splash-brand">
    <div class="brand-dot"></div>
    <div class="splash-name">MARLOWICK</div>
    <div class="splash-tagline">SECURITY THROUGH TRANPARENCY</div>
  </div>
</section>

<section class="screen screen--login" aria-label="Log in screen">
  <div class="status-bar"><span class="signal">●●●●●</span><span>11:47</span><span>86% <i class="battery"></i></span></div>
  <div class="login-brand">
    <div class="brand-dot"></div>
    <div class="name">MARLOWICK</div>
  </div>
  <label class="field field--email">
    <svg width="18" height="13" viewBox="0 0 18 13" fill="none" stroke="#9a9a9a"><rect x=".5" y=".5" width="17" height="12" rx="1"/><path d="M1 1l8 6 8-6"/></svg>
    <span>User email</span>
  </label>
  <label class="field field--pin">
    <svg width="16" height="18" viewBox="0 0 16 18" fill="none" stroke="#9a9a9a"><rect x="1" y="7.5" width="14" height="10" rx="1"/><path d="M4 7.5V5a4 4 0 018 0v2.5"/><path d="M8 11v3"/></svg>
    <span>PIN</span>
    <svg class="trail" width="22" height="16" viewBox="0 0 22 16" fill="none" stroke="#8a8a8a" stroke-width="1.4"><path d="M1 8s4-6 10-6 10 6 10 6-4 6-10 6S1 8 1 8z"/><circle cx="11" cy="8" r="3"/><path d="M17 1L5 15"/></svg>
  </label>
  <button class="btn-login">LOG IN</button>
  <p class="forgot"><u>Forgot</u> your password?</p>
  <p class="signup">Don't have account? <b>SIGN UP</b> for Marlowick</p>
</section>

<section class="screen screen--chats" aria-label="Chat list screen">
  <header class="chat-header">
    <div class="status-bar"><span class="signal">●●●●●</span><span>11:47</span><span>86% <i class="battery"></i></span></div>
    <div class="toolbar">
      <svg width="20" height="12" viewBox="0 0 20 12" stroke="#fff"><path d="M0 1h20M0 6h20M0 11h20"/></svg>
      <div class="tabs"><span class="tab">All</span><span class="tab">Student</span><span class="tab">Parent</span><span class="tab">Teacher</span></div>
      <svg width="20" height="18" viewBox="0 0 20 18" fill="none" stroke="#fff"><path d="M1 1h18v12H7l-4 4v-4H1z"/><path d="M10 4v6M7 7h6"/></svg>
    </div>
  </header>
  <ul class="chat-list">
    <li class="chat-item"><div class="avatar" role="img" aria-label="Profile photo"></div><div class="chat-body"><div class="chat-top"><span><b>Harry T</b> (Parrent)</span><span class="chat-time">06.30 PM</span></div><div class="chat-preview">Lorem ipsum dolor sit amet, consectetuer</div></div></li>
    <li class="chat-item"><div class="avatar" role="img" aria-label="Profile photo"></div><div class="chat-body"><div class="chat-top"><span><b>Dicky C</b> (Parrent)</span><span class="chat-time">03.20 PM</span></div><div class="chat-preview">Lorem ipsum dolor sit amet, consectetuer</div></div></li>
    <li class="chat-item"><div class="avatar" role="img" aria-label="Profile photo"></div><div class="chat-body"><div class="chat-top"><span><b>Tommy</b> (Teacher)</span><span class="chat-time">02.55 PM</span></div><div class="chat-preview">Lorem ipsum dolor sit amet, consectetuer</div></div></li>
    <li class="chat-item"><div class="avatar" role="img" aria-label="Profile photo"></div><div class="chat-body"><div class="chat-top"><span><b>Lorenzo</b> (Teacher)</span><span class="chat-time">02.40 PM</span></div><div class="chat-preview">Lorem ipsum dolor sit amet, consectetuer</div></div></li>
    <li class="chat-item"><div class="avatar" role="img" aria-label="Profile photo"></div><div class="chat-body"><div class="chat-top"><span><b>Dina Mariana</b> (Teacher)</span><span class="chat-time">02.20 PM</span></div><div class="chat-preview">Lorem ipsum dolor sit amet, consectetuer</div></div></li>
    <li class="chat-item"><div class="avatar" role="img" aria-label="Profile photo"></div><div class="chat-body"><div class="chat-top"><span><b>Julie Estele</b> (Student)</span><span class="chat-time">01.30 AM</span></div><div class="chat-preview">Lorem ipsum dolor sit amet, consectetuer</div></div></li>
    <li class="chat-item"><div class="avatar" role="img" aria-label="Profile photo"></div><div class="chat-body"><div class="chat-top"><span><b>Gopal D</b> (Student)</span><span class="chat-time">Yesterday</span></div><div class="chat-preview">Lorem ipsum dolor sit amet, consectetuer</div></div></li>
    <li class="chat-item"><div class="avatar" role="img" aria-label="Profile photo"></div><div class="chat-body"><div class="chat-top"><span><b>Dean Hotman</b> (Parrent)</span><span class="chat-time">Yesterday</span></div><div class="chat-preview">Lorem ipsum dolor sit amet, consectetuer</div></div></li>
  </ul>
  <nav class="tab-bar">
    <div class="tab-bar__item"><svg width="30" height="26" viewBox="0 0 30 26"><path d="M1 1h28v18H10l-6 6v-6H1z" fill="#0a6fe3"/></svg>Chat</div>
    <div class="tab-bar__item"><svg width="22" height="22" viewBox="0 0 22 22" fill="none" stroke="#6d6d6d"><circle cx="6" cy="6" r="4"/><circle cx="16" cy="6" r="4"/><circle cx="6" cy="16" r="4"/><circle cx="16" cy="16" r="4"/></svg>Discover</div>
    <div class="tab-bar__item"><svg width="24" height="24" viewBox="0 0 24 24" fill="none" stroke="#6d6d6d"><rect x="3" y="1" width="20" height="22"/><circle cx="13" cy="9" r="3.5"/><path d="M7 19c1-4 11-4 12 0M1 6h4M1 12h4M1 18h4"/></svg>Contact</div>
    <div class="tab-bar__item"><svg width="24" height="26" viewBox="0 0 24 26" fill="none" stroke="#6d6d6d"><path d="M6 4l2-3 3 2c5 0 8 5 8 10l4 6-21 5 2-7c-2-4-2-10 2-13z"/><path d="M9 23a3 3 0 006-1"/></svg>Notification</div>
    <div class="tab-bar__item"><svg width="24" height="24" viewBox="0 0 24 24" fill="none" stroke="#6d6d6d"><circle cx="12" cy="12" r="4"/><path d="M12 1v4M12 19v4M1 12h4M19 12h4M4.2 4.2l2.8 2.8M17 17l2.8 2.8M4.2 19.8L7 17M17 7l2.8-2.8"/><circle cx="12" cy="12" r="8"/></svg>Setting</div>
  </nav>
</section>

</body>
</html>
```